mailer to distressed properties

Our business is a company that buys houses for cash that are in need of repairs. Need to create a post card to mail to homeowners to get them to call us to give them a price on their home for cash and purchase it. Would like a run down house on background and our company info so they could call us. Have a logo would like to incorporate in it. Want to get to the point across we can buy there home for cash on any condition and close quickly. We can also buy them if they have permit or violation issues. We also buy homes going into foreclosure so we can stop foreclosure. Company name is R & T Dwellings. P o box 829 Westmere my 11947. 631-482-9163. Email us at info@randtdwellings.example and our website Randtdwellings.example. Open to a lot of direct designs excited to see what you come up with. Anything else you can think we are open to see it. Email us with any other questions . Also can add fast closing and save no real estate commissions collected. We want it in color your choice. Also on font open to anything and size of font.

Target Market(s)

Run down and distressed properties

Industry/Entity Type

Construction Company

Font styles to use
Serif
Sans Serif

Requirements
Must have
• A background of a distressed home and our info how to call us
Nice to have
• Colorful and attractive
Should not have
• Nothing I can think of

```html
<!DOCTYPE html>
<html lang="en">
<head>
<meta charset="utf-8">
<title>R &amp; T Dwellings – Postcard Mailer</title>
<link href="https://fonts.googleapis.com/css2?family=Oswald:wght@700&family=PT+Sans:wght@400;700&family=PT+Sans+Narrow:wght@400;700&family=Signika:wght@400;600;700&display=swap" rel="stylesheet">
<style>
  :root{
    --red:#e4141b;
    --red-dark:#a8191c;
    --yellow:#fdd32b;
    --orange:#f6a12d;
    --ink:#1d1d1d;
    --panel:rgba(18,18,18,.86);
    --paper:#ffffff;
    --paper-grey:#f2f2f2;
    --line:#c9c9c9;
    --page:#e9e6e1;
  }
  *{box-sizing:border-box;margin:0;padding:0}
  html,body{width:1073px;height:1200px;overflow:hidden;background:var(--page)}
  .canvas{position:relative;width:1073px;height:1200px}
  .card{position:absolute;left:106px;width:860px;height:557px;overflow:hidden;box-shadow:0 6px 16px rgba(0,0,0,.28)}
  .card--front{top:30px}
  .card--back{top:637px;background:var(--paper)}

  /* front */
  .front-photo{position:absolute;inset:0;background:
      linear-gradient(180deg,#6f98c9 0%,#9fb9d6 30%,#cfcfcc 55%,#8f8a80 78%,#5b5a4e 100%)}
  .front-photo__cash{position:absolute;left:520px;top:40px;width:330px;height:430px;border-radius:6px;
      background:linear-gradient(160deg,#f4f4f1 0%,#d9dbd6 55%,#b9a58f 100%)}
  .top-band{position:absolute;left:0;top:0;width:100%;height:24px;background:linear-gradient(180deg,#ef2a23,#c8161b)}
  .front-panel{position:absolute;left:40px;top:24px;width:320px;height:523px;background:var(--panel);text-align:center;color:#fff}
  .front-name{margin-top:28px;font:400 33px/1 "PT Sans",sans-serif;color:#fff}
  .front-name-rule{width:250px;height:1px;margin:14px auto 0;background:rgba(255,255,255,.35)}
  .front-kicker{margin-top:20px;font:700 17px/17px "PT Sans",sans-serif;letter-spacing:1.6px;text-align:left;padding-left:48px}
  .front-cash{margin-top:2px;font:700 78px/1 "Oswald",sans-serif;text-align:left;padding-left:44px;
      background:linear-gradient(180deg,#ffe55a 0%,#fbb51e 100%);-webkit-background-clip:text;background-clip:text;color:transparent}
  .front-sub{margin-top:40px;font:400 23px/1 "PT Sans Narrow",sans-serif}
  .checklist{list-style:none;text-align:left;margin:22px 0 0 28px}
  .checklist li{display:flex;align-items:center;gap:12px;font:400 18px/1 "PT Sans Narrow",sans-serif;margin-bottom:12px}
  .tick{width:16px;height:16px;flex:none}
  .phone-bar{position:absolute;left:33px;top:438px;width:332px;height:50px;background:linear-gradient(180deg,#f0262a,#c4161b);
      display:flex;align-items:center;justify-content:center;gap:10px;color:#fff;font:700 27px/1 "PT Sans",sans-serif;box-shadow:0 3px 6px rgba(0,0,0,.4)}
  .front-web{position:absolute;left:40px;top:497px;width:320px;text-align:center;color:#fff;font:700 14px/1 "PT Sans",sans-serif;letter-spacing:1px}
  .phone-icon{width:26px;height:26px;flex:none}
  .condition-band{position:absolute;left:457px;top:497px;width:403px;height:60px;border-radius:14px 0 0 0;
      background:linear-gradient(180deg,var(--yellow),var(--orange));display:flex;align-items:center;justify-content:center;
      color:var(--red);font:400 17px/1 "PT Sans Narrow",sans-serif}

  /* back */
  .back-shape{position:absolute;left:0;top:0}
  .back-name{position:absolute;left:0;top:126px;width:520px;text-align:center;font:700 40px/1 "Signika",sans-serif;color:var(--ink)}
  .back-banner{position:absolute;left:0;top:171px;width:552px;height:120px;background:linear-gradient(180deg,#ee2327,#c1161b);
      text-align:center;box-shadow:0 3px 5px rgba(0,0,0,.3)}
  .back-banner__line1{margin-top:20px;font:600 35px/1 "Signika",sans-serif;color:#fff}
  .back-banner__line2{margin-top:9px;font:600 35px/1 "Signika",sans-serif;color:var(--yellow)}
  .back-copy{position:absolute;left:33px;top:302px;width:462px;font:400 16.5px/19.5px "PT Sans",sans-serif;color:var(--ink);letter-spacing:-.2px}
  .back-contact{position:absolute;left:0;top:392px;width:470px;height:96px;text-align:center}
  .back-contact__phone{display:flex;align-items:center;justify-content:center;gap:12px;margin-top:16px;margin-left:-10px;
      font:700 38px/1 "PT Sans",sans-serif;color:var(--red)}
  .back-contact__web{margin-top:8px;font:700 23px/1 "PT Sans",sans-serif;color:var(--ink);letter-spacing:1.5px;margin-left:-20px}
  .return-address{position:absolute;left:550px;top:34px;font:400 11.5px/15px "PT Sans",sans-serif;color:var(--ink);font-style:normal}
  .return-address__name{font-size:15px;line-height:18px}
  .stamp-box{position:absolute;left:740px;top:33px;width:104px;height:66px;border:1.5px solid var(--line)}
  .address-lines{position:absolute;left:586px;top:202px;width:258px}
  .address-lines span{display:block;height:1.5px;background:var(--line);margin-bottom:35px}
</style>
</head>
<body>
<div class="canvas">

  <section class="card card--front">
    <div class="front-photo" role="img" aria-label="Run-down white clapboard farmhouse under a blue sky">
      <div class="front-photo__cash" role="img" aria-label="Hand holding a fan of hundred-dollar bills"></div>
    </div>
    <div class="top-band"></div>
    <div class="front-panel">
      <div class="front-name">R &amp; T Dwellings</div>
      <div class="front-name-rule"></div>
      <div class="front-kicker">QUICKLY SELL YOUR<br>HOUSE FAST FOR</div>
      <div class="front-cash">CA$H!</div>
      <div class="front-sub">We'll Buy Your Home</div>
      <ul class="checklist">
        <li><svg class="tick" viewBox="0 0 16 16"><circle cx="8" cy="8" r="8" fill="#f7b82a"/><path d="M4.5 8.3l2.3 2.3 4.7-5" stroke="#fff" stroke-width="2" fill="none"/></svg>WITH CASH</li>
        <li><svg class="tick" viewBox="0 0 16 16"><circle cx="8" cy="8" r="8" fill="#f7b82a"/><path d="M4.5 8.3l2.3 2.3 4.7-5" stroke="#fff" stroke-width="2" fill="none"/></svg>IN ANY CONDITION</li>
        <li><svg class="tick" viewBox="0 0 16 16"><circle cx="8" cy="8" r="8" fill="#f7b82a"/><path d="M4.5 8.3l2.3 2.3 4.7-5" stroke="#fff" stroke-width="2" fill="none"/></svg>FORECLOSURE</li>
        <li><svg class="tick" viewBox="0 0 16 16"><circle cx="8" cy="8" r="8" fill="#f7b82a"/><path d="M4.5 8.3l2.3 2.3 4.7-5" stroke="#fff" stroke-width="2" fill="none"/></svg>PERMIT OR VIOLATION ISSUES</li>
      </ul>
    </div>
    <div class="phone-bar">
      <svg class="phone-icon" viewBox="0 0 26 26"><rect width="26" height="26" rx="5" fill="#f7b82a"/><path d="M8 5.5c1 0 2 2.6 2.2 3.5.2.9-1.3 1.5-1.1 2.3.5 1.8 2.8 4.2 4.6 4.7.8.2 1.4-1.3 2.3-1.1.9.2 3.5 1.2 3.5 2.2 0 1.5-1.6 3.4-3.4 3.3C11 20 6 15 5.1 9 4.9 7.3 6.6 5.5 8 5.5z" fill="#c4161b"/></svg>
      631-482-9163
    </div>
    <div class="front-web">www.randtdwellings.example</div>
    <div class="condition-band">ANY CONDITION, ANY SITUATION, ANY PROBLEM</div>
  </section>

  <section class="card card--back">
    <svg class="back-shape" width="560" height="557" viewBox="0 0 560 557">
      <path d="M0 0H440C520 60 545 200 525 290C505 380 460 440 400 488H0Z" fill="#f2f2f2"/>
      <path d="M440 0H470C545 90 560 220 530 320C505 400 455 450 400 488C470 420 520 320 520 230C515 120 480 50 440 0Z" fill="#b7191c"/>
    </svg>
    <div class="back-name">R &amp; T Dwellings</div>
    <div class="back-banner">
      <div class="back-banner__line1">QUICKLY SELL YOUR HOUSE</div>
      <div class="back-banner__line2">FAST FOR CASH</div>
    </div>
    <p class="back-copy">We'll give you top dollar for your house, accept it in any condition, and take you through the whole process quickly. Our team is local and made up of licensed and insured home builders and real estate professionals who have a proven track record.</p>
    <svg class="back-shape" style="top:392px" width="470" height="96" viewBox="0 0 470 96">
      <defs><linearGradient id="bandGrad" x1="0" x2="1"><stop offset="0" stop-color="#fdd32b"/><stop offset="1" stop-color="#f6a12d"/></linearGradient></defs>
      <path d="M0 0H466L395 96H0Z" fill="url(#bandGrad)"/>
    </svg>
    <div class="back-contact">
      <div class="back-contact__phone">
        <svg class="phone-icon" style="width:34px;height:34px" viewBox="0 0 26 26"><rect width="26" height="26" rx="5" fill="#e4141b"/><path d="M8 5.5c1 0 2 2.6 2.2 3.5.2.9-1.3 1.5-1.1 2.3.5 1.8 2.8 4.2 4.6 4.7.8.2 1.4-1.3 2.3-1.1.9.2 3.5 1.2 3.5 2.2 0 1.5-1.6 3.4-3.4 3.3C11 20 6 15 5.1 9 4.9 7.3 6.6 5.5 8 5.5z" fill="#f7b82a"/></svg>
        631-482-9163
      </div>
      <div class="back-contact__web">www.randtdwellings.example</div>
    </div>
    <address class="return-address">
      <div class="return-address__name">R &amp; T Dwellings</div>
      P.O. Box 829<br>Westmere NY 11947<br>631-482-9163<br>info@randtdwellings.example
    </address>
    <div class="stamp-box"></div>
    <div class="address-lines"><span></span><span></span><span></span><span></span><span></span></div>
  </section>

</div>
</body>
</html>
```